Google slides for an upcoming presentation

I would like to recreate the jpeg to better match our company branding & color, as well as better resolution-- which is found in the PPTX. The slide should read....
"What are the biggest differences between Web 2.0 to Web 3.0"

Industry/Entity Type

Web3

Other font styles liked:
• Manrope

```html
<!DOCTYPE html>
<html lang="en">
<head>
<meta charset="UTF-8">
<title>What are the biggest differences between Web 2.0 to Web 3.0</title>
<link rel="stylesheet" href="https://fonts.googleapis.com/css2?family=Montserrat:wght@500;600;700;800&display=swap">
<style>
  :root {
    --ink: #0c2844;
    --glow: rgba(225, 240, 255, 0.9);
    --pill-light-top: #f2f9fd;
    --pill-light-bottom: #cfe8f7;
    --pill-light-text: #124a7a;
    --pill-blue-top: #71c6ef;
    --pill-blue-bottom: #2690dd;
    --pill-blue-text: #ffffff;
    --bg-warm: #e8d6cc;
    --bg-rose: #dcc3bd;
    --bg-lilac: #c9b8e4;
  }
  * { margin: 0; padding: 0; box-sizing: border-box; }
  html, body { width: 1200px; height: 675px; overflow: hidden; }
  body { font-family: "Montserrat", Arial, sans-serif; background: var(--bg-warm); }

  .slide { position: relative; width: 1200px; height: 675px; overflow: hidden; }

  .scene-art {
    position: absolute; inset: 0;
    background:
      radial-gradient(ellipse 60% 50% at 15% 85%, rgba(180, 160, 235, 0.55), transparent 70%),
      radial-gradient(ellipse 70% 30% at 40% 30%, rgba(235, 215, 245, 0.6), transparent 70%),
      linear-gradient(180deg, #e9dbd1 0%, var(--bg-rose) 45%, #e4d4cf 75%, var(--bg-lilac) 100%);
  }

  .headline {
    position: absolute; left: 0; right: 0; top: 88px;
    text-align: center; color: var(--ink);
    text-shadow: 0 0 6px var(--glow), 0 0 2px var(--glow);
    letter-spacing: -0.5px;
  }
  .headline-line { display: block; line-height: 1; }
  .headline-line--first { font-size: 94px; font-weight: 600; }
  .headline-line--first .minor { font-size: 56px; font-weight: 500; margin: 0 6px; }
  .headline-line--second { font-size: 73px; font-weight: 500; margin-top: 10px; }

  .comparison {
    position: absolute; left: 83px; top: 319px; width: 1029px; height: 128px;
    display: flex; align-items: center; justify-content: space-between;
  }
  .pill {
    width: 439px; height: 128px; border-radius: 64px;
    display: flex; align-items: center; justify-content: center;
    font-size: 80px; font-weight: 800; letter-spacing: 1px;
    box-shadow: 0 6px 18px rgba(60, 80, 120, 0.18);
  }
  .pill--current {
    background: linear-gradient(180deg, var(--pill-light-top) 0%, #e1f1fa 45%, var(--pill-light-bottom) 100%);
    color: var(--pill-light-text);
  }
  .pill--next {
    background: linear-gradient(180deg, var(--pill-blue-top) 0%, #4eaee9 45%, var(--pill-blue-bottom) 100%);
    color: var(--pill-blue-text);
  }
  .connector {
    font-size: 46px; font-weight: 600; color: var(--ink);
    text-shadow: 0 0 6px var(--glow);
  }

  .reflection {
    position: absolute; left: 83px; top: 452px; width: 1029px; height: 128px;
    display: flex; justify-content: space-between;
    transform: scaleY(-1); opacity: 0.28;
    -webkit-mask-image: linear-gradient(0deg, #000 0%, transparent 75%);
    mask-image: linear-gradient(0deg, #000 0%, transparent 75%);
  }
  .reflection .pill { box-shadow: none; }
</style>
</head>
<body>
  <main class="slide">
    <div class="scene-art" role="img" aria-label="Soft pastel 3D city network with glowing light trails sweeping across"></div>

    <h1 class="headline">
      <span class="headline-line headline-line--first">What<span class="minor">are the</span>biggest</span>
      <span class="headline-line headline-line--second">differences between</span>
    </h1>

    <div class="comparison">
      <div class="pill pill--current">WEB 2.0</div>
      <span class="connector">to</span>
      <div class="pill pill--next">WEB 3.0</div>
    </div>

    <div class="reflection" aria-hidden="true">
      <div class="pill pill--current">WEB 2.0</div>
      <div class="pill pill--next">WEB 3.0</div>
    </div>
  </main>
</body>
</html>
```